Create a flyer that will catch your eye and make you want to call us for KELVANE seamless Gutters

We are looking for a logo to help us with sales of our seamless gutter business, we are looking to expand, add loyal customers and increase our referral business.
We provide a turn key process from sales to install. we show up with our rolling factory, our truck spits out what seems to be an endless supply of gutter!
Each job is fabricated and installed to meet your homes design.

Target Market(s)

Treasure Coast of Florida, single story Homes

Font styles to use
Serif

Requirements
Must have
• Our Logo and Name on the flyer
Clean design with a clear message
call to action

```html
<!DOCTYPE html>
<html lang="en">
<head>
<meta charset="utf-8">
<title>Kelvane Gutter Works – Flyer</title>
<link rel="stylesheet" href="https://fonts.googleapis.com/css2?family=Anton&family=Exo+2:wght@400;500;600&display=swap">
<style>
  :root{
    --green:#0f8f3c;
    --grey-text:#7a7a7a;
    --ink:#2b2b2b;
    --panel:#ecedee;
    --haze:#b8d6e8;
    --sky-top:#5c9cc6;
    --sky-deep:#1d5f96;
    --wall:#c79a6a;
    --wall-light:#e8c9a3;
    --white:#ffffff;
  }
  *{margin:0;padding:0;box-sizing:border-box}
  html,body{width:849px;height:1200px;overflow:hidden;background:var(--white)}
  .flyer{position:relative;width:849px;height:1200px;overflow:hidden;font-family:"Exo 2",sans-serif;color:var(--ink)}
  .hero-photo{position:absolute;inset:0;background:linear-gradient(135deg,var(--sky-top) 0%,var(--sky-deep) 38%,var(--wall) 52%,var(--wall-light) 80%,var(--wall) 100%)}
  .panels{position:absolute;inset:0;width:849px;height:1200px}
  .brand{position:absolute;left:48px;top:150px;display:flex;align-items:center;gap:16px}
  .brand-dot{width:64px;height:64px;border-radius:50%;background:#9a9a9a}
  .brand-name{font-family:"Anton",sans-serif;font-size:50px;color:var(--green);letter-spacing:.5px;line-height:1}
  .headline{position:absolute;left:15px;top:700px;font-family:"Anton",sans-serif;color:var(--green);font-size:26px;line-height:37px;letter-spacing:.3px}
  .subhead{position:absolute;left:15px;top:776px;font-family:"Anton",sans-serif;color:var(--grey-text);font-size:14.5px;letter-spacing:.2px}
  .body-copy{position:absolute;left:15px;top:815px;width:372px;font-size:13.6px;line-height:18.4px;text-align:justify}
  .body-copy p{margin-bottom:18.4px}
  .mascot{position:absolute;left:392px;top:800px;width:228px;height:400px;background:linear-gradient(180deg,#d9e9dc 0%,#3fa661 60%,#0f8f3c 100%);border-radius:110px 110px 0 0}
  .estimate-card{position:absolute;left:605px;top:947px;width:228px;height:233px;background:var(--white);border-radius:10px;padding:18px 16px 0 16px}
  .bracket{position:absolute;width:26px;height:26px;border:2.5px solid var(--green)}
  .bracket.tl{left:16px;top:20px;border-right:none;border-bottom:none}
  .bracket.br{right:16px;bottom:20px;border-left:none;border-top:none}
  .free{font-size:38px;font-weight:500;color:var(--green);letter-spacing:6px;line-height:1;padding-left:12px}
  .free-sub{font-size:11.5px;font-weight:500;letter-spacing:.3px;padding-left:12px;margin-top:2px;margin-bottom:14px}
  .office{font-size:10.6px;line-height:13.8px;margin-bottom:9px}
  .office dl{display:grid;grid-template-columns:74px auto}
</style>
</head>
<body>
<main class="flyer">
  <div class="hero-photo" role="img" aria-label="Photograph of a single-story home eave with a tan seamless gutter and downspout against a blue sky"></div>

  <svg class="panels" viewBox="0 0 849 1200" aria-hidden="true">
    <polygon points="0,313 309,561 309,733 0,480" fill="var(--haze)" opacity=".85"/>
    <polygon points="0,480 309,733 415,1200 0,1200" fill="var(--panel)"/>
    <polygon points="0,560 30,580 309,785 309,800" fill="var(--white)" opacity=".9"/>
    <polygon points="280,1070 415,1200 280,1200" fill="var(--white)"/>
  </svg>

  <div class="brand">
    <span class="brand-dot"></span>
    <span class="brand-name">Kelvane Gutter Works</span>
  </div>

  <h1 class="headline">COMPREHENSIVE<br>VERSATILE SOLUTIONS</h1>
  <h2 class="subhead">FOR ALL YOUR GUTTER REQUIREMENTS</h2>

  <div class="body-copy">
    <p>Kelvane Gutter Works provides top quality seamless gutter system that will protect your home for many years. Our traveling gutter factory on wheels allows us to custom fit gutters to your homes specific needs at a competitive price. We take pride in our excellent customer service, professional installs and quality products.</p>
    <p>Someone is always available to answer your calls, provide answers to your questions and update you on the progress of your job.</p>
    <p>We provide the very best warranty in the business and use the best materials available.</p>
    <p>We provide FREE in home estimates and are adhering to stringent covid-19 protocals.</p>
  </div>

  <div class="mascot" role="img" aria-label="Cartoon installer in a green cap and overalls with arms crossed"></div>

  <aside class="estimate-card">
    <span class="bracket tl"></span>
    <span class="bracket br"></span>
    <div class="free">FREE</div>
    <div class="free-sub">IN-HOME ESTIMATES</div>
    <div class="office">
      1820 Harbor Pine Lane<br>Palm Harbor, Florida 34900
      <dl><dt>Phone</dt><dd>555-014-2277</dd><dt>Fax</dt><dd>555-014-3390</dd></dl>
    </div>
    <div class="office">
      312 Coral Reef Avenue<br>Palm Harbor, Florida 34900
      <dl><dt>Phone</dt><dd>555-014-2277</dd><dt>Fax</dt><dd>555-014-3390</dd></dl>
    </div>
  </aside>
</main>
</body>
</html>
```